Rack Card for Bright Oak Dog Training

I love the logo you designed for me a while back (I had it updated and have the new files).

I need a rack card designed, 2 sided.

One side will be Bright Oak Dog Training (my general dog training business)

The other side will be my Deaf and Blind Dog Training Business speciality.

Both sides Full Color/4 color

3.5 x 8.5 inches

I can provide photos and text accordingly.

Let me know the estimated price and Turn around time.

```html
<!DOCTYPE html>
<html lang="en">
<head>
<meta charset="utf-8">
<title>Bright Oak Dog Training – Rack Card, Both Sides</title>
<link href="https://fonts.googleapis.com/css2?family=Poppins:wght@400;500;600;700;800&family=Allura&display=swap" rel="stylesheet">
<style>
  :root {
    --page: #ececec;
    --ink: #121212;
    --orange: #fca311;
    --orange-deep: #e08e00;
    --white: #ffffff;
    --panel: #ebebeb;
    --text-dark: #1a1a1a;
    --rule: #5a5a5a;
    --wave-line: #d9d2bd;
    --logo-grey: #3a3a3a;
    --paw: #9a9a9a;
  }
  * { margin: 0; padding: 0; box-sizing: border-box; }
  html, body { width: 686px; height: 1200px; overflow: hidden; background: var(--page); }
  body { font-family: "Poppins", sans-serif; position: relative; }

  .rack-card {
    position: absolute; top: 217px;
    width: 478px; height: 1160px;
    background: var(--ink); overflow: hidden;
    transform: scale(.66); transform-origin: 0 0;
    box-shadow: 0 6px 18px rgba(0,0,0,.18);
  }
  .rack-card.front { left: 18px; }
  .rack-card.back { left: 352px; }

  .hero-photo { position: absolute; left: 0; top: 0; width: 478px; height: 500px; }
  .front .hero-photo { background: linear-gradient(180deg, #cfe3f2 0%, #dde8ee 45%, #a9b08a 68%, #6f7a45 100%); }
  .back .hero-photo { background: linear-gradient(180deg, #e3e7ea 0%, #dfe4e6 22%, #b8ccd3 30%, #cbbba5 48%, #a98a6c 70%, #8a6a4d 100%); }

  .brand-mark {
    position: absolute; left: 0; top: 92px; width: 478px;
    display: flex; justify-content: center; align-items: center; gap: 10px;
  }
  .brand-mark .dot { width: 14px; height: 14px; border-radius: 50%; background: var(--logo-grey); }
  .brand-mark .name { font-weight: 500; font-size: 26px; color: var(--logo-grey); letter-spacing: .5px; }

  .wave { position: absolute; left: 0; }
  .front .wave { top: 420px; }
  .back .wave { top: 418px; }

  .photo-circle {
    position: absolute; border-radius: 50%;
    border: 6px solid var(--orange-deep);
    box-shadow: 0 0 0 2px var(--ink);
  }
  .photo-circle.owner-pups { left: 195px; top: 390px; width: 140px; height: 140px; background: radial-gradient(circle at 45% 40%, #e2c2a2 0%, #b7855a 55%, #8fa3c7 100%); }
  .photo-circle.black-lab { left: 303px; top: 436px; width: 122px; height: 122px; background: radial-gradient(circle at 50% 45%, #3a3a3a 0%, #1c1c1c 60%, #4d5a3b 100%); }
  .photo-circle.trainer-lead { left: 193px; top: 369px; width: 160px; height: 160px; background: radial-gradient(circle at 50% 45%, #d9c7a6 0%, #9fb07a 55%, #5f8a3f 100%); }
  .photo-circle.golden { left: 313px; top: 443px; width: 122px; height: 122px; background: radial-gradient(circle at 50% 50%, #c98c4e 0%, #9a5f30 60%, #6b4225 100%); }

  .paws { display: inline-flex; gap: 2px; align-items: flex-start; margin-bottom: 6px; }

  .headline { position: absolute; left: 46px; color: var(--white); }
  .front .headline { top: 520px; }
  .headline .script { font-family: "Allura", cursive; font-size: 66px; line-height: 1; display: block; margin-bottom: -8px; }
  .headline .accent { font-weight: 800; font-size: 62px; line-height: 1; color: var(--orange); display: block; letter-spacing: -.5px; }
  .headline .plain { font-weight: 800; font-size: 52px; line-height: 1.05; display: flex; align-items: flex-end; gap: 14px; letter-spacing: -.3px; }
  .back .headline { top: 538px; }
  .back .headline .lead { display: block; font-size: 40px; line-height: 1.1; letter-spacing: -.3px; }
  .back .headline .lead b { font-weight: 800; }
  .back .headline .lead span { font-weight: 500; }
  .back .headline .accent { font-size: 60px; }

  .rule { position: absolute; left: 46px; width: 392px; height: 1px; background: var(--rule); }
  .rule-tab { position: absolute; width: 54px; height: 5px; border-radius: 3px; background: var(--orange); }
  .front .rule { top: 693px; }
  .front .rule-tab { top: 691px; left: 212px; }
  .back .rule { top: 702px; }
  .back .rule-tab { top: 700px; left: 212px; }

  /* front */
  .intro { position: absolute; left: 30px; top: 714px; width: 418px; text-align: center; color: var(--white); }
  .intro h2 { font-weight: 700; font-size: 17px; color: var(--orange); letter-spacing: .3px; }
  .intro p { font-size: 11px; line-height: 1.28; margin-top: 4px; }

  .services { position: absolute; left: 37px; top: 822px; width: 403px; height: 160px; background: var(--panel); border-radius: 18px; }
  .services-tab {
    position: absolute; left: 76px; top: 802px; width: 318px; height: 44px;
    background: var(--orange); border-radius: 0 0 28px 28px;
    display: flex; align-items: center; justify-content: center; text-align: center;
    font-weight: 700; font-size: 15px; line-height: 1.05; color: var(--text-dark);
  }
  .services-tab::before, .services-tab::after { content: ""; position: absolute; top: 0; width: 14px; height: 14px; background: var(--orange-deep); }
  .services-tab::before { left: -10px; border-radius: 14px 0 0 0; }
  .services-tab::after { right: -10px; border-radius: 0 14px 0 0; }
  .service-list { position: absolute; list-style: none; color: var(--text-dark); font-weight: 500; font-size: 15px; top: 864px; }
  .service-list li { display: flex; align-items: center; gap: 7px; height: 23px; }
  .service-list.left { left: 62px; }
  .service-list.right { left: 226px; }
  .service-list.right li { height: 26px; }
  .tick { width: 10px; height: 10px; flex: none; }

  .puppy-photo {
    position: absolute; left: 356px; top: 932px; width: 122px; height: 82px;
    border-radius: 50px 0 0 40px;
    background: linear-gradient(120deg, #f1f1f1 0%, #b9b9b9 45%, #5c5c5c 100%);
  }

  .trainer { position: absolute; left: 0; top: 1004px; width: 478px; text-align: center; color: var(--white); }
  .trainer .label { font-size: 13px; letter-spacing: 3px; }
  .trainer .name { font-weight: 600; font-size: 19px; letter-spacing: .4px; }

  /* back */
  .care-copy { position: absolute; left: 46px; top: 729px; width: 246px; color: var(--white); font-size: 11px; line-height: 13.5px; }
  .care-copy p + p { margin-top: 8px; }
  .service-dog-photo {
    position: absolute; left: 303px; top: 726px; width: 141px; height: 178px;
    border: 2px solid var(--white); border-radius: 5px;
    background: linear-gradient(160deg, #7d8f5a 0%, #cfd3c8 40%, #f2f2f2 60%, #7a6a55 100%);
  }
  .specialty-box {
    position: absolute; left: 34px; top: 937px; width: 410px; height: 66px;
    border: 1px solid var(--white); border-radius: 6px;
    color: var(--white); text-align: center;
  }
  .specialty-box h2 {
    position: absolute; left: 50%; top: -9px; transform: translateX(-50%);
    background: var(--ink); padding: 0 6px; white-space: nowrap;
    font-weight: 700; font-size: 12.5px; line-height: 16px; color: var(--orange);
  }
  .specialty-box p { font-size: 11px; line-height: 13.5px; margin-top: 20px; padding: 0 40px; }
  .contact-title { position: absolute; left: 0; top: 1023px; width: 478px; text-align: center; color: var(--white); font-weight: 600; font-size: 19px; }

  /* shared footer */
  .phone-pill {
    position: absolute; left: 43px; top: 1055px; width: 392px; height: 39px;
    background: var(--orange); border-radius: 20px;
    display: flex; align-items: center; padding-left: 8px; color: var(--text-dark);
  }
  .phone-icon { width: 30px; height: 30px; border-radius: 50%; background: var(--white); display: flex; align-items: center; justify-content: center; flex: none; }
  .numbers { display: flex; align-items: flex-end; margin-left: 12px; gap: 4px; }
  .number { display: flex; flex-direction: column; line-height: 1; }
  .number small { font-size: 7px; font-weight: 700; letter-spacing: .2px; }
  .number strong { font-size: 20px; font-weight: 700; letter-spacing: .3px; }
  .slash { font-size: 22px; font-weight: 700; line-height: 1; }
  .website { position: absolute; left: 0; top: 1106px; width: 478px; text-align: center; color: var(--white); font-weight: 500; font-size: 16px; letter-spacing: 1.6px; }
</style>
</head>
<body>
  <!-- Side one: general training -->
  <section class="rack-card front">
    <div class="hero-photo" role="img" aria-label="Photo of a trainer guiding a black dog over an agility jump in a grassy field"></div>
    <div class="brand-mark"><span class="dot"></span><span class="name">Bright Oak</span></div>

    <svg class="wave" width="478" height="120" viewBox="0 0 478 120">
      <path d="M0 100 C 60 78, 130 68, 200 78 C 270 88, 330 112, 400 98 C 440 90, 460 80, 478 72 L478 120 L0 120 Z" fill="var(--wave-line)"/>
      <path d="M0 106 C 60 84, 130 74, 200 84 C 270 94, 330 118, 400 104 C 440 96, 460 86, 478 78 L478 120 L0 120 Z" fill="var(--ink)"/>
    </svg>

    <div class="photo-circle owner-pups" role="img" aria-label="Photo of a smiling owner holding two puppies"></div>
    <div class="photo-circle black-lab" role="img" aria-label="Portrait photo of a black Labrador"></div>

    <h1 class="headline">
      <span class="script">Bright</span>
      <span class="accent">OAK DOG</span>
      <span class="plain">TRAINING
        <span class="paws" aria-hidden="true">
          <svg width="30" height="28" viewBox="0 0 30 28" fill="var(--paw)"><ellipse cx="15" cy="19" rx="8" ry="7"/><circle cx="5" cy="11" r="3.6"/><circle cx="11" cy="5" r="3.6"/><circle cx="19" cy="5" r="3.6"/><circle cx="25" cy="11" r="3.6"/></svg>
          <svg width="20" height="19" viewBox="0 0 30 28" fill="var(--paw)"><ellipse cx="15" cy="19" rx="8" ry="7"/><circle cx="5" cy="11" r="3.6"/><circle cx="11" cy="5" r="3.6"/><circle cx="19" cy="5" r="3.6"/><circle cx="25" cy="11" r="3.6"/></svg>
        </span>
      </span>
    </h1>

    <div class="rule"></div>
    <div class="rule-tab"></div>

    <section class="intro">
      <h2>BRIGHT OAK</h2>
      <p>Training is my passion and my profession! I have been handling, training and caring for animals for most of my life. I spent many successful years in corporate life and have returned to my true love, training.</p>
    </section>

    <div class="services"></div>
    <div class="services-tab">DOG TRAINING &amp;<br>BEHAVIORAL SERVICES</div>

    <ul class="service-list left">
      <li><svg class="tick" viewBox="0 0 10 10"><circle cx="5" cy="5" r="5" fill="var(--orange)"/><path d="M2.8 5.2 L4.4 6.7 L7.3 3.6" stroke="#fff" stroke-width="1.3" fill="none"/></svg>Puppy Training</li>
      <li><svg class="tick" viewBox="0 0 10 10"><circle cx="5" cy="5" r="5" fill="var(--orange)"/><path d="M2.8 5.2 L4.4 6.7 L7.3 3.6" stroke="#fff" stroke-width="1.3" fill="none"/></svg>House Breaking</li>
      <li><svg class="tick" viewBox="0 0 10 10"><circle cx="5" cy="5" r="5" fill="var(--orange)"/><path d="M2.8 5.2 L4.4 6.7 L7.3 3.6" stroke="#fff" stroke-width="1.3" fill="none"/></svg>Leash Training</li>
      <li><svg class="tick" viewBox="0 0 10 10"><circle cx="5" cy="5" r="5" fill="var(--orange)"/><path d="M2.8 5.2 L4.4 6.7 L7.3 3.6" stroke="#fff" stroke-width="1.3" fill="none"/></svg>Obedience</li>
    </ul>
    <ul class="service-list right">
      <li><svg class="tick" viewBox="0 0 10 10"><circle cx="5" cy="5" r="5" fill="var(--orange)"/><path d="M2.8 5.2 L4.4 6.7 L7.3 3.6" stroke="#fff" stroke-width="1.3" fill="none"/></svg>Rescue Dog Training</li>
      <li><svg class="tick" viewBox="0 0 10 10"><circle cx="5" cy="5" r="5" fill="var(--orange)"/><path d="M2.8 5.2 L4.4 6.7 L7.3 3.6" stroke="#fff" stroke-width="1.3" fill="none"/></svg>Separation Anxiety</li>
      <li><svg class="tick" viewBox="0 0 10 10"><circle cx="5" cy="5" r="5" fill="var(--orange)"/><path d="M2.8 5.2 L4.4 6.7 L7.3 3.6" stroke="#fff" stroke-width="1.3" fill="none"/></svg>Socialization</li>
    </ul>

    <div class="puppy-photo" role="img" aria-label="Photo of a merle puppy lying down with its head on its paws"></div>

    <section class="trainer">
      <p class="label">Meet the Trainer</p>
      <p class="name">MAREN ELLIS HOLT</p>
    </section>

    <div class="phone-pill">
      <span class="phone-icon"><svg width="16" height="16" viewBox="0 0 24 24"><path d="M6.6 10.8c1.4 2.8 3.8 5.1 6.6 6.6l2.2-2.2c.3-.3.7-.4 1-.2 1.1.4 2.3.6 3.6.6.6 0 1 .4 1 1V20c0 .6-.4 1-1 1C10.6 21 3 13.4 3 4c0-.6.4-1 1-1h3.5c.6 0 1 .4 1 1 0 1.3.2 2.5.6 3.6.1.3 0 .7-.2 1L6.6 10.8z" fill="var(--text-dark)"/></svg></span>
      <div class="numbers">
        <span class="number"><small>LOS ANGELES</small><strong>310-555-0147</strong></span>
        <span class="slash">/</span>
        <span class="number"><small>ORANGE COUNTY</small><strong>714-555-0192</strong></span>
      </div>
    </div>
    <p class="website">www.brightoakdogtraining.com</p>
  </section>

  <!-- Side two: deaf and blind specialty -->
  <section class="rack-card back">
    <div class="hero-photo" role="img" aria-label="Photo of a happy brown and white Australian shepherd on a beach"></div>
    <div class="brand-mark"><span class="dot"></span><span class="name">Bright Oak</span></div>

    <svg class="wave" width="478" height="120" viewBox="0 0 478 120">
      <path d="M0 96 C 50 78, 110 70, 170 86 C 230 102, 300 112, 380 96 C 420 88, 455 78, 478 74 L478 120 L0 120 Z" fill="var(--wave-line)"/>
      <path d="M0 102 C 50 84, 110 76, 170 92 C 230 108, 300 118, 380 102 C 420 94, 455 84, 478 80 L478 120 L0 120 Z" fill="var(--ink)"/>
    </svg>

    <div class="photo-circle trainer-lead" role="img" aria-label="Photo of a trainer fitting an orange leash on a light-coloured dog in a park"></div>
    <div class="photo-circle golden" role="img" aria-label="Portrait photo of a golden retriever being petted"></div>

    <h1 class="headline">
      <span class="lead"><b>DEAF</b> <span>AND</span></span>
      <span class="accent">BLIND DOG</span>
      <span class="plain">TRAINING
        <span class="paws" aria-hidden="true">
          <svg width="30" height="28" viewBox="0 0 30 28" fill="var(--paw)"><ellipse cx="15" cy="19" rx="8" ry="7"/><circle cx="5" cy="11" r="3.6"/><circle cx="11" cy="5" r="3.6"/><circle cx="19" cy="5" r="3.6"/><circle cx="25" cy="11" r="3.6"/></svg>
          <svg width="20" height="19" viewBox="0 0 30 28" fill="var(--paw)"><ellipse cx="15" cy="19" rx="8" ry="7"/><circle cx="5" cy="11" r="3.6"/><circle cx="11" cy="5" r="3.6"/><circle cx="19" cy="5" r="3.6"/><circle cx="25" cy="11" r="3.6"/></svg>
        </span>
      </span>
    </h1>

    <div class="rule"></div>
    <div class="rule-tab"></div>

    <section class="care-copy">
      <p>Deaf/Blind dogs can easily be trained using touch and tactile cues.</p>
      <p>We owe it to our dogs to teach them how to behave, to know their surroundings even when their sight and hearing is lost, and that the world is a safe place.</p>
      <p>A dog with special needs is no exception.</p>
      <p>Training a dog that is both blind and deaf can come with its own challenges, we have many years of experience to help.</p>
    </section>

    <div class="service-dog-photo" role="img" aria-label="Photo of a white service dog wearing a blue vest beside a tree"></div>

    <section class="specialty-box">
      <h2>WE SPECIALIZE IN DEAF AND BLIND DOG TRAINING</h2>
      <p>Our Private One-on-One Blind Dog Training is a rewarding experience for you and your dog.</p>
    </section>

    <p class="contact-title">CONTACT US</p>

    <div class="phone-pill">
      <span class="phone-icon"><svg width="16" height="16" viewBox="0 0 24 24"><path d="M6.6 10.8c1.4 2.8 3.8 5.1 6.6 6.6l2.2-2.2c.3-.3.7-.4 1-.2 1.1.4 2.3.6 3.6.6.6 0 1 .4 1 1V20c0 .6-.4 1-1 1C10.6 21 3 13.4 3 4c0-.6.4-1 1-1h3.5c.6 0 1 .4 1 1 0 1.3.2 2.5.6 3.6.1.3 0 .7-.2 1L6.6 10.8z" fill="var(--text-dark)"/></svg></span>
      <div class="numbers">
        <span class="number"><small>LOS ANGELES</small><strong>310-555-0147</strong></span>
        <span class="slash">/</span>
        <span class="number"><small>ORANGE COUNTY</small><strong>714-555-0192</strong></span>
      </div>
    </div>
    <p class="website">www.brightoakdogtraining.com</p>
  </section>
</body>
</html>
```